ZoVEX App logo & homescreen design

We are creating a new app call "ZoVEX" that is designed for young adults (15-24 years old) to create a sexual risk reduction plan to help young adults follow their relationship goals while also being safe. Currently, we need graphic design for the ZoVEX: (1) app logo and (2) a home screen for the app. We would like to see designs that are appealing to the target population - young adults ages 15-24. These requests are only the beginning of a series of graphic designs needs that I have to develop the app - and will offer one-on-one graphic design opportunities (much more $$$ to come) for the right graphic designer. The ZoVEX app is complimentary follow-up to another commercial app we have call KALDRO, designed for doctors to assess young adults' level of sexual risk during a dr. appointment (see vantrolibsoft.com for more details) after leaving a doctors visit. I have uploaded our company branding guidelines, but am open to any colors, fonts that are appealing to the target population.

Target Market(s)

youth 15-24 years of age

Industry/Entity Type

Health And Wellness

Colors

Designer to choose colors to be used in the design.

Requirements
Must have
• Both MUST be appealing to the target market.
• The app logo should be an icon or image that represents a plan.
• The homescreen UI needs to be easy to navigate and include 4 key sections: (1) Info - this section will include educational information tailored to their sexual risk level, (2) Plan - this section will link them to create their sexual risk reduction plan, (3) Sharing - this section will link them to areas that allow them to share their plan with their doctor or others, and (4) tip - this section may be a link OR the main part of the homescreen that shares daily/weekly tips on how to stick to their plan. I suggest getting inspiration from https://www.brindelfolio.com/30-recent-inspirational-ui-examples-in-mobile-device-screens.html.
Nice to have
• In app design focus groups, youth in the target market suggested that it would should have a similar look and feel to fizzlor because they LOVE that app.
Should not have
• imply its a sexual related or healthcare/wellness related - want to to seem fun & easy to use. I open to any ideas here and am looking for YOU to be CREATIVE!!!

```html
<!DOCTYPE html>
<html lang="en">
<head>
<meta charset="utf-8">
<title>ZoVEX – Home screen variants</title>
<link rel="stylesheet" href="https://fonts.googleapis.com/css2?family=Nunito:wght@400;600;700;800&display=swap">
<style>
  :root {
    --page-bg: #ffffff;
    --screen-bg: #15162d;
    --card-bg: #1b1c37;
    --pill-bg: #1f2040;
    --text-light: #ffffff;
    --text-soft: #e7e7ef;
    --ink-dark: #1a1b33;
    --accent-purple: #7a22a3;
    --tile-dark: #1d1e3b;
    --photo-top: #3b3440;
    --photo-mid: #2e3a58;
    --photo-warm: #5a3f3a;
  }
  * { box-sizing: border-box; margin: 0; padding: 0; }
  html, body {
    width: 1200px; height: 698px; overflow: hidden;
    background: var(--page-bg);
    font-family: "Nunito", sans-serif;
  }
  .showcase { position: relative; width: 1200px; height: 698px; }

  .screen {
    position: absolute; top: 42px;
    width: 344px; height: 616px;
    border-radius: 16px; overflow: hidden;
    background: var(--screen-bg);
    color: var(--text-light);
    box-shadow: 0 4px 14px rgba(20, 20, 40, 0.18);
  }
  .screen--light  { left: 32px;  --tile-bg: #ffffff;              --tile-ink: var(--ink-dark); }
  .screen--purple { left: 428px; --tile-bg: var(--accent-purple); --tile-ink: #ffffff; }
  .screen--dark   { left: 822px; --tile-bg: var(--tile-dark);     --tile-ink: #ffffff; }

  .hero-photo {
    position: absolute; left: 0; top: 0; width: 100%; height: 280px;
    background:
      radial-gradient(ellipse 60% 45% at 30% 35%, var(--photo-warm) 0%, transparent 70%),
      radial-gradient(ellipse 70% 55% at 70% 40%, var(--photo-mid) 0%, transparent 75%),
      linear-gradient(180deg, var(--photo-top) 0%, #272a45 55%, var(--screen-bg) 100%);
    opacity: 0.9;
  }

  .brand {
    position: absolute; left: 0; right: 0; top: 130px;
    text-align: center;
    font-weight: 800; font-size: 31px; letter-spacing: 0.5px;
    color: var(--text-light);
  }

  .tip-heading {
    position: absolute; left: 22px; top: 240px;
    display: flex; align-items: center; gap: 8px;
    font-size: 17.5px; font-weight: 400; letter-spacing: 0.3px;
  }
  .tip-heading svg { width: 10px; height: 14px; }

  .tip-card {
    position: absolute; left: 14px; top: 273px;
    width: 318px; height: 143px;
    border-radius: 12px;
    background: var(--card-bg);
    padding: 7px 22px 0 23px;
  }
  .tip-title { font-size: 13.6px; font-weight: 700; margin-bottom: 5px; }
  .tip-body {
    font-size: 11px; line-height: 15.8px;
    text-align: justify; color: var(--text-soft);
  }

  .pager {
    position: absolute; left: 282px; top: 426px;
    width: 50px; height: 15px; border-radius: 8px;
    background: var(--pill-bg);
    display: flex; justify-content: center; align-items: center; gap: 8px;
  }
  .pager span { width: 5px; height: 5px; border-radius: 50%; background: #fff; }

  .nav {
    position: absolute; left: 14px; top: 461px;
    display: flex; gap: 11px;
  }
  .nav-tile {
    width: 99px; height: 98px; border-radius: 13px;
    background: var(--tile-bg); color: var(--tile-ink);
    display: flex; flex-direction: column; align-items: center;
    padding-top: 28px;
  }
  .nav-tile svg { width: 30px; height: 30px; }
  .nav-tile span { margin-top: 10px; font-size: 13px; font-weight: 400; }

  .maker {
    position: absolute; left: 0; right: 0; top: 592px;
    text-align: center;
    font-size: 11px; font-weight: 600; color: var(--text-light);
  }
</style>
</head>
<body>
<main class="showcase">

  <!-- Screen 1: light tiles -->
  <section class="screen screen--light">
    <div class="hero-photo" role="img" aria-label="Blurred photo of a young person in jeans, sitting"></div>
    <div class="brand">ZoVEX</div>
    <h2 class="tip-heading">
      <svg viewBox="0 0 10 14" fill="none" stroke="#fff" stroke-width="1.2"><circle cx="5" cy="5" r="4"/><path d="M3.5 9v2.5h3V9M4 13h2"/></svg>
      Tip of the day
    </h2>
    <article class="tip-card">
      <h3 class="tip-title">Act early</h3>
      <p class="tip-body">Pulse Digest explains that 62 percent of teens who said that they drank reported they had their first drink before the age of 15 – not including simply taking a sip. This is why it is best for parents to talk to their kids about drugs and drinking around age 12, 13 or 14, since it is likely they will already have been offered substances by then.</p>
    </article>
    <div class="pager"><span></span><span></span><span></span></div>
    <nav class="nav">
      <a class="nav-tile">
        <svg viewBox="0 0 30 30" fill="none" stroke="currentColor" stroke-width="2.2" stroke-linejoin="round"><path d="M4 4h22v17H15l-5 5v-5H4z"/><path d="M15 8v7M15 17.5v.5" stroke-linecap="round"/></svg>
        <span>Info</span>
      </a>
      <a class="nav-tile">
        <svg viewBox="0 0 30 30" fill="none" stroke="currentColor" stroke-width="2.2" stroke-linejoin="round" stroke-linecap="round"><path d="M4 4v22h23"/><path d="M7 21l6-9 5 5 7-11"/></svg>
        <span>Plan</span>
      </a>
      <a class="nav-tile">
        <svg viewBox="0 0 30 30" fill="currentColor" stroke="currentColor" stroke-width="2.2"><circle cx="22" cy="6" r="4"/><circle cx="7" cy="15" r="4"/><circle cx="22" cy="24" r="4"/><path d="M22 6L7 15l15 9" fill="none"/></svg>
        <span>Share</span>
      </a>
    </nav>
    <footer class="maker">Lumenhart</footer>
  </section>

  <!-- Screen 2: purple tiles -->
  <section class="screen screen--purple">
    <div class="hero-photo" role="img" aria-label="Blurred photo of a young person in jeans, sitting"></div>
    <div class="brand">ZoVEX</div>
    <h2 class="tip-heading">
      <svg viewBox="0 0 10 14" fill="none" stroke="#fff" stroke-width="1.2"><circle cx="5" cy="5" r="4"/><path d="M3.5 9v2.5h3V9M4 13h2"/></svg>
      Tip of the day
    </h2>
    <article class="tip-card">
      <h3 class="tip-title">Act early</h3>
      <p class="tip-body">Pulse Digest explains that 62 percent of teens who said that they drank reported they had their first drink before the age of 15 – not including simply taking a sip. This is why it is best for parents to talk to their kids about drugs and drinking around age 12, 13 or 14, since it is likely they will already have been offered substances by then.</p>
    </article>
    <div class="pager"><span></span><span></span><span></span></div>
    <nav class="nav">
      <a class="nav-tile">
        <svg viewBox="0 0 30 30" fill="none" stroke="currentColor" stroke-width="2.2" stroke-linejoin="round"><path d="M4 4h22v17H15l-5 5v-5H4z"/><path d="M15 8v7M15 17.5v.5" stroke-linecap="round"/></svg>
        <span>Info</span>
      </a>
      <a class="nav-tile">
        <svg viewBox="0 0 30 30" fill="none" stroke="currentColor" stroke-width="2.2" stroke-linejoin="round" stroke-linecap="round"><path d="M4 4v22h23"/><path d="M7 21l6-9 5 5 7-11"/></svg>
        <span>Plan</span>
      </a>
      <a class="nav-tile">
        <svg viewBox="0 0 30 30" fill="currentColor" stroke="currentColor" stroke-width="2.2"><circle cx="22" cy="6" r="4"/><circle cx="7" cy="15" r="4"/><circle cx="22" cy="24" r="4"/><path d="M22 6L7 15l15 9" fill="none"/></svg>
        <span>Share</span>
      </a>
    </nav>
    <footer class="maker">Lumenhart</footer>
  </section>

  <!-- Screen 3: dark tiles -->
  <section class="screen screen--dark">
    <div class="hero-photo" role="img" aria-label="Blurred photo of a young person in jeans, sitting"></div>
    <div class="brand">ZoVEX</div>
    <h2 class="tip-heading">
      <svg viewBox="0 0 10 14" fill="none" stroke="#fff" stroke-width="1.2"><circle cx="5" cy="5" r="4"/><path d="M3.5 9v2.5h3V9M4 13h2"/></svg>
      Tip of the day
    </h2>
    <article class="tip-card">
      <h3 class="tip-title">Act early</h3>
      <p class="tip-body">Pulse Digest explains that 62 percent of teens who said that they drank reported they had their first drink before the age of 15 – not including simply taking a sip. This is why it is best for parents to talk to their kids about drugs and drinking around age 12, 13 or 14, since it is likely they will already have been offered substances by then.</p>
    </article>
    <div class="pager"><span></span><span></span><span></span></div>
    <nav class="nav">
      <a class="nav-tile">
        <svg viewBox="0 0 30 30" fill="none" stroke="currentColor" stroke-width="2.2" stroke-linejoin="round"><path d="M4 4h22v17H15l-5 5v-5H4z"/><path d="M15 8v7M15 17.5v.5" stroke-linecap="round"/></svg>
        <span>Info</span>
      </a>
      <a class="nav-tile">
        <svg viewBox="0 0 30 30" fill="none" stroke="currentColor" stroke-width="2.2" stroke-linejoin="round" stroke-linecap="round"><path d="M4 4v22h23"/><path d="M7 21l6-9 5 5 7-11"/></svg>
        <span>Plan</span>
      </a>
      <a class="nav-tile">
        <svg viewBox="0 0 30 30" fill="currentColor" stroke="currentColor" stroke-width="2.2"><circle cx="22" cy="6" r="4"/><circle cx="7" cy="15" r="4"/><circle cx="22" cy="24" r="4"/><path d="M22 6L7 15l15 9" fill="none"/></svg>
        <span>Share</span>
      </a>
    </nav>
    <footer class="maker">Lumenhart</footer>
  </section>

</main>
</body>
</html>
```